Elegant & Eye-Catching Brochure- Photo Booth Rentals

We rent photo booths for weddings, sweet 16's, parties, mitzvah's, school and corporate events and we would like to create a vibrant and fun, yet professional brochure to be attractive to the entire spectrum of potential clients. The brochure will be the standard tri-fold style (8.5"x11") and will have 3 inside panels and 3 outside panels.

Ideally this brochure would be elegant, classy, and professional, but still vibrant and fun. We have many colorful images that convey the quality of our photos and options, we want to highlight that aspect, but also would like to maintain that we are a great selection for weddings. Thus we stress the classy yet fun aspect of this project. Also, it would be preferable to use legible and interesting, but clear fonts. Clean and less cluttered is also a plus, but by all means just do what you think looks best.

Attached are the photos that we have available and fit our goals. There is no need to use them all, but if possible please stress the great range of options and the lovely clean wedding shots. Blue, White, Silver and a splash of pink have been used in the past for our logo, site, business cards, and older brochures so those are the preferred colors for this brochure. This brochure should trend feminine. Most of our clients are brides and mothers so that should be taken into consideration, but only to a point so that we don't close ourselves off to anyone.

I am attaching a logo, some photos strips, single shots, and instructions on the actual wording. Please let me know if you need anything else. Thank you in advance.
Updates

Target Market(s)

most of our clients are female, but the brochure shouldn't be so feminine as to dissuade males from becoming clients

Industry/Entity Type

School

Colors
f9d9e8
ffffff
f0f0f0
86cae7

Requirements
Nice to have
• A way of fitting in a variety of colorful photos to highlight our range, but while still maintaining a clean and ordered look.

```html
<!DOCTYPE html>
<html lang="en">
<head>
<meta charset="utf-8">
<title>Harborlight Photo Booths – Tri-fold Brochure</title>
<link rel="stylesheet" href="https://fonts.googleapis.com/css2?family=Barlow:wght@500;600&family=Source+Sans+3:wght@400;600;700&family=Oswald:wght@400;500&display=swap">
<style>
  :root {
    --blue: #1fa3dc;
    --cyan: #2ad3e6;
    --cyan-light: #5fdcec;
    --card: rgba(214, 238, 250, 0.92);
    --silver: #e4e4e4;
    --silver-light: #f4f4f4;
    --pink-soft: #f9d9e8;
    --ink: #1c1c1c;
    --grey-text: #7d7f82;
    --white: #ffffff;
  }
  * { margin: 0; padding: 0; box-sizing: border-box; }
  html, body { width: 1200px; height: 894px; overflow: hidden; background: var(--white); }
  .brochure { position: relative; width: 1200px; height: 894px; overflow: hidden; font-family: "Source Sans 3", sans-serif; color: var(--ink); }

  .inside-backdrop { position: absolute; left: 0; top: 0; width: 799px; height: 894px; }

  .venue-photo { position: absolute; left: 23px; top: 0; width: 328px; height: 212px;
    background: linear-gradient(165deg, #3b4c63 0%, #7b98b3 45%, #5fc9e0 78%, #34495e 100%); }

  .welcome-card { position: absolute; left: 24px; top: 212px; width: 327px; height: 616px;
    background: var(--card); border-radius: 0 0 10px 10px; box-shadow: 0 2px 6px rgba(0,0,0,0.25);
    padding: 55px 24px 0; text-align: center; font-size: 15.5px; line-height: 27.1px; color: #222; }
  .welcome-card p + p { margin-top: 27px; }

  .company-header { position: absolute; left: 351px; top: 0; width: 448px; height: 60px; background: var(--cyan);
    font-family: "Oswald", sans-serif; font-weight: 500; font-size: 33px; color: var(--white);
    padding: 10px 0 0 21px; line-height: 40px; }

  .company-intro { position: absolute; left: 377px; top: 108px; width: 405px; font-size: 16.5px; line-height: 28px; color: #2a2a2a; }

  .services-title { position: absolute; left: 376px; top: 300px; font-family: "Oswald", sans-serif; font-weight: 400;
    font-size: 18.5px; color: var(--ink); }
  .services-list { position: absolute; left: 377px; top: 329px; list-style: none; font-weight: 600; font-size: 15px; line-height: 27px; }
  .services-list li::before { content: "• "; }

  .award-badge { position: absolute; left: 570px; top: 520px; width: 215px; height: 193px;
    background: linear-gradient(135deg, var(--white) 0%, var(--pink-soft) 55%, #eef6fb 100%); }

  .hours { position: absolute; left: 372px; top: 656px; font-weight: 700; font-size: 20px; color: var(--white); }
  .hq-name { position: absolute; left: 377px; top: 746px; font-weight: 700; font-size: 17px; color: var(--white); }
  .hq-city { position: absolute; left: 382px; top: 779px; font-size: 14px; color: var(--white); }

  .cover { position: absolute; left: 799px; top: 0; width: 401px; height: 894px;
    background: linear-gradient(180deg, #dadada 0%, var(--silver) 45%, var(--silver-light) 100%); }
  .cover-art { position: absolute; left: 0; top: 0; width: 401px; height: 460px; }
  .cover-title { position: absolute; left: 0; top: 533px; width: 401px; text-align: center;
    font-family: "Barlow", sans-serif; font-weight: 500; color: var(--blue); letter-spacing: 1px; }
  .cover-title .name { font-size: 25px; line-height: 34px; }
  .cover-title .tagline { font-size: 25px; line-height: 32px; margin-top: 12px; }

  .brand-mark { position: absolute; left: 0; top: 735px; width: 401px; display: flex; justify-content: center; align-items: center; gap: 10px;
    font-family: "Barlow", sans-serif; font-weight: 600; font-size: 22px; color: var(--grey-text); }
  .brand-mark .dot { width: 16px; height: 16px; border-radius: 50%; background: var(--grey-text); }

  .web-bar { position: absolute; left: 0; bottom: 0; width: 401px; height: 49px; background: var(--cyan-light);
    text-align: right; padding: 11px 32px 0 0; font-weight: 700; font-size: 18px; color: var(--ink); }
</style>
</head>
<body>
<main class="brochure">

  <svg class="inside-backdrop" viewBox="0 0 799 894" role="img" aria-label="Faded photo of a waterfront event venue with guests and a photo booth">
    <defs>
      <linearGradient id="venueWash" x1="0" y1="0" x2="1" y2="1">
        <stop offset="0" stop-color="#cfe3ee"/>
        <stop offset="0.5" stop-color="#b3d6e8"/>
        <stop offset="1" stop-color="#d9ebf3"/>
      </linearGradient>
    </defs>
    <rect width="799" height="894" fill="url(#venueWash)"/>
    <path d="M0 498 C110 560 250 598 370 582 C560 556 700 430 799 252 L799 894 L0 894 Z" fill="var(--blue)"/>
  </svg>

  <div class="venue-photo" role="img" aria-label="Photo of a photo booth set up at an evening event overlooking a city skyline"></div>

  <section class="welcome-card">
    <p>We are so happy you made it to our web site! A little about us- Harborlight Photo Booth is a family run company that has provided the region with award winning services for many years. We have been a part of thousands of events and maintained a 5 Star Rating on every major review site and a healthy base of happy repeat clients.</p>
    <p>We hope that you will take a peak around our site and become our next happy client. Please take some time to look around and learn about the many options that we provide. At the end we hope you will send us an inquiry so that we can provide you with an affordable quote, and perfect package tailored just for your event. Enjoy!</p>
  </section>

  <h2 class="company-header">OUR COMPANY</h2>
  <p class="company-intro">In searching for a suitable Photo Booth company, it is often difficult to put one's faith and trust in a company or brand, especially when you are searching through vendors online. This page is intended to give you a little background on Harborlight Photo Booths, our successes, and track record of excellence.</p>

  <h3 class="services-title">Our Services List</h3>
  <ul class="services-list">
    <li>Services List 1</li>
    <li>Services List 2</li>
    <li>Services List 3</li>
    <li>Services List 4</li>
    <li>Services List 5</li>
  </ul>

  <div class="award-badge" role="img" aria-label="Wedding award badge with bouquet and gown photos"></div>

  <p class="hours">Specialist 24/7/365</p>
  <p class="hq-name">Brightway Headquarters</p>
  <p class="hq-city">Millbrook, NJ</p>

  <section class="cover">
    <svg class="cover-art" viewBox="0 0 401 460" role="img" aria-label="Photo of a cheerful bride and groom showing off the ring">
      <defs>
        <linearGradient id="coupleTone" x1="0" y1="0" x2="1" y2="1">
          <stop offset="0" stop-color="#cfcfd1"/>
          <stop offset="0.55" stop-color="#b4b4b8"/>
          <stop offset="1" stop-color="#e6e2de"/>
        </linearGradient>
      </defs>
      <path d="M0 0 H401 V440 C300 425 150 390 0 255 Z" fill="url(#coupleTone)"/>
      <path d="M0 255 C150 390 300 425 401 440" fill="none" stroke="var(--blue)" stroke-width="6"/>
    </svg>

    <div class="cover-title">
      <p class="name">HARBORLIGHT PHOTO BOOTHS</p>
      <p class="tagline">MAKE MEMORIES ON<br>YOUR SPECIAL DAY</p>
    </div>

    <div class="brand-mark"><span class="dot"></span>Harborlight Photo Booths</div>

    <div class="web-bar">www.harborlightbooths.com</div>
  </section>

</main>
</body>
</html>
```